KEV.PRO- Darren Holcombe Fitness- needs a clever business card using the logo, name, info, contact

I need a business card designed for my Online Personal Training company called KEV.PRO, abbreviation for Darren Holcombe Fitness. My company focuses on coaching in personal health and personal growth to unleash your greatest potential. I would like to see designs that use my color scheme of a redish-orange (C:0,M:84,Y:100,K:0), grey, white, black, and my company font is OSWALD. The final design should communicate some aspects of design, health, motivation, growth, in some way. The logo is very important to the company and can be displayed in any of the colors previously mentioned. Must include the company name, my website: www.kev-pro.example , my email: dan@kev-pro.example

Target Market(s)

Personal health, fitness, general public, those who lack knowledge, awareness, and confidence in personal health

Industry/Entity Type

Personal Trainer

Font styles to use
Other font styles liked:
• OSWALD. (Bold, Regular, Light)

Colors
f37122
ffffff
9d9d9d
000000

Requirements
Must have
• Must include the logo, company name, my website: www.kev-pro.example , my email: dan@kev-pro.example
Nice to have
• Variations of the colors scheme of a redish-orange (C:0,M:84,Y:100,K:0), grey, white, black. Logo, card, or text can be in any of these colors.
• Possible quote like "Take control of your personal health to unleash your greatest potential" or "Unleashing your greatness first begins with fitness of the body and mind"

```html
<!DOCTYPE html>
<html lang="en">
<head>
<meta charset="utf-8">
<title>KEV.PRO Business Card</title>
<link href="https://fonts.googleapis.com/css2?family=Oswald:wght@300;400;700&family=Roboto+Condensed:wght@400&family=Roboto:wght@400;500&display=swap" rel="stylesheet">
<style>
  :root {
    --orange: #f04e23;
    --ink: #231f20;
    --white: #ffffff;
    --paper: #f6f6f6;
    --grey: #9d9d9d;
    --text-dark: #3b3b3b;
    --backdrop: #8a8a8a;
    --mark-faint: #3c2624;
  }
  html, body {
    margin: 0;
    width: 1200px;
    height: 960px;
    overflow: hidden;
    background: var(--backdrop);
  }
  .stage { position: relative; width: 1200px; height: 960px; }
  .card {
    position: absolute;
    width: 600px;
    height: 342px;
    overflow: hidden;
    box-shadow: 0 3px 6px rgba(0,0,0,.35);
  }
  /* Front */
  .card-front { left: 314px; top: 113px; background: var(--paper); }
  .card-front .wave { position: absolute; left: 0; top: 0; }
  .brand-block {
    position: absolute; left: 138px; top: 74px; width: 116px;
    text-align: center;
  }
  .brand-ring {
    width: 104px; height: 104px; margin: 0 auto;
    border: 8px solid var(--orange); border-radius: 50%;
    box-sizing: border-box;
  }
  .brand-name {
    margin-top: 16px;
    font: 700 21px/1 "Oswald", sans-serif;
    color: var(--ink);
  }
  .brand-sub {
    margin-top: 3px;
    font: 400 5px/1 "Oswald", sans-serif;
    color: var(--ink);
    letter-spacing: .2px;
  }
  .divider {
    position: absolute; left: 284px; top: 75px;
    width: 1px; height: 146px; background: var(--orange);
  }
  .person { position: absolute; left: 318px; top: 88px; }
  .person-name {
    font: 500 21px/1 "Roboto Condensed", sans-serif;
    color: var(--orange); margin: 0;
  }
  .person-role {
    font: 500 15px/1 "Roboto", sans-serif;
    color: var(--ink); margin: 6px 0 0;
  }
  .contact-list { list-style: none; margin: 16px 0 0; padding: 0; }
  .contact-list li {
    display: flex; align-items: center; gap: 8px;
    font: 400 14px/19px "Roboto", sans-serif; color: var(--text-dark);
  }
  .contact-list svg { width: 13px; height: 13px; flex: none; }
  .tagline {
    position: absolute; left: 0; right: 0; top: 296px;
    text-align: center; color: var(--white);
    font: 400 13.5px/19px "Roboto Condensed", sans-serif;
  }
  .tagline p { margin: 0; }
  /* Back */
  .card-back { left: 311px; top: 472px; background: var(--ink); }
  .back-ring {
    position: absolute; left: 283px; top: 8px;
    width: 318px; height: 318px; border-radius: 50%;
    border: 14px solid var(--mark-faint); box-sizing: border-box;
  }
  .back-name {
    position: absolute; left: 31px; top: 228px; margin: 0;
    font: 700 64px/1 "Oswald", sans-serif; color: var(--white);
  }
  .back-sub {
    position: absolute; left: 32px; top: 298px; margin: 0;
    font: 300 19px/1 "Oswald", sans-serif; color: var(--white);
  }
</style>
</head>
<body>
<div class="stage">
  <section class="card card-front">
    <svg class="wave" width="600" height="342" viewBox="0 0 600 342" aria-hidden="true">
      <path d="M0 226 Q300 330 600 226 L600 342 L0 342 Z" fill="var(--orange)"/>
      <path d="M18 232 Q300 324 600 228" fill="none" stroke="var(--ink)" stroke-width="3"/>
    </svg>
    <div class="brand-block">
      <div class="brand-ring"></div>
      <div class="brand-name">KEV.PRO</div>
      <div class="brand-sub">DARREN HOLCOMBE FITNESS</div>
    </div>
    <div class="divider"></div>
    <div class="person">
      <h1 class="person-name">JORDAN REYES</h1>
      <p class="person-role">CEO/FOUNDER</p>
      <ul class="contact-list">
        <li><svg viewBox="0 0 24 24"><path fill="var(--orange)" d="M6.6 10.8a15 15 0 0 0 6.6 6.6l2.2-2.2a1 1 0 0 1 1-.25 11.4 11.4 0 0 0 3.6.6 1 1 0 0 1 1 1V20a1 1 0 0 1-1 1A17 17 0 0 1 3 4a1 1 0 0 1 1-1h3.5a1 1 0 0 1 1 1c0 1.25.2 2.45.6 3.6a1 1 0 0 1-.25 1z"/></svg>555 014 2290</li>
        <li><svg viewBox="0 0 24 24"><path fill="var(--orange)" d="M2 5h20v14H2z"/><path fill="none" stroke="var(--paper)" stroke-width="2" d="M2 6l10 7 10-7"/></svg>dan@kev-pro.example</li>
        <li><svg viewBox="0 0 24 24"><circle cx="12" cy="12" r="10" fill="var(--orange)"/><path fill="none" stroke="var(--paper)" stroke-width="1.6" d="M2 12h20M12 2c3 3 3 17 0 20M12 2c-3 3-3 17 0 20"/></svg>www.kev-pro.example</li>
      </ul>
    </div>
    <div class="tagline">
      <p>Take control of your personal health to unleash your greatest potential</p>
      <p>Unleashing your greatness first begins with fitness of the body and mind</p>
    </div>
  </section>

  <section class="card card-back">
    <div class="back-ring" aria-hidden="true"></div>
    <h2 class="back-name">KEV.PRO</h2>
    <p class="back-sub">DARREN HOLCOMBE.FITNESS</p>
  </section>
</div>
</body>
</html>
```